The Harborline LLC Asset Classes

I'm looking for for two designs here to go into powerpoint and potentially as a standalone PDF. My company does wealth management.
Graphic Image #1
I break down the investment world into 4 broad categories
-Preservation
-Capital Markets
-Real Estate
-Alternatives
In each broad category, there are subcategories:
Preservation: cash, checking/savings accounts, money market accounts, CD's, and fixed annuities.
Capital Markets: Publicly traded stocks and bonds
Real Estate: single-family residence, retail, industrial, multifamily, and office
Alternatives: private equity, private credit, cryptocurrency, asset-backed loans, tax liens, oil & gas, litigation finance, and royalties
Graphic 2: Please see the bottom f page 1 of the Tidewater Slides PDF.
Just like in graphic one, you have 4 categories of the Capital Markets and their respective subcategories
Category 1: Domestic Stocks: Subcategories are Large, mid, and small size companies
Category 2: International Stocks: Subcategories are Large, Mid/Small and by region - Developed and Emerging
Category 3: Fixed Income: You have subcategories like corporate, municipal, government, domestic, international
Category 4: Alternatives: The subcategories are metals and real estate
---------------------
I'm looking to create a graphic (either pie chart, or a circle broken into parts or some other clever way to illustrate this) to clearly illustrate both of these universes in a clean, professional, slick manner.
Target Market(s)
Investors
Colors
Designer to choose colors to be used in the design.
Requirements
Must have
- Clean
- professional
- Easy to read
- Creative
- Visually appealling
Nice to have
- I have attached my logo and some marketing materials so you can get a feel of what I am doing. Maybe you can clean this up too!

```html
<!DOCTYPE html>
<html lang="en">
<head>
<meta charset="utf-8">
<title>The Harborline LLC – Asset Classes</title>
<link rel="stylesheet" href="https://fonts.googleapis.com/css2?family=Libre+Baskerville:wght@400;700&family=Lato:wght@400&display=swap">
<style>
  :root{
    --page:#e4e4e7;
    --white:#ffffff;
    --navy-title:#1d5d93;
    --green:#2e8b3e;
    --navy:#0d4a6b;
    --orange:#e0952a;
    --gray:#949699;
    --teal:#2a93b4;
    --teal-deep:#156a8a;
    --panel:#ececec;
    --ink:#222;
    --line:#a9a9a9;
  }
  *{margin:0;padding:0;box-sizing:border-box}
  html,body{width:1200px;height:1200px;overflow:hidden;background:var(--page)}
  .canvas{position:relative;width:1200px;height:1200px}
  .slide-frame{position:absolute;left:162px;width:876px;height:492px;overflow:hidden;background:var(--white)}
  .slide-frame--first{top:46px}
  .slide-frame--second{top:580px}
  .slide{position:absolute;left:0;top:0;width:984px;height:553px;transform:scale(0.8902);transform-origin:0 0}
  .slide-art{position:absolute;left:0;top:0;width:984px;height:553px}
  .slide-title{position:absolute;left:35px;top:14px;font-family:"Libre Baskerville",serif;font-weight:700;font-size:46px;color:var(--navy-title);letter-spacing:.5px}
  .brand{position:absolute;right:44px;top:52px;display:flex;align-items:center;gap:10px}
  .brand-dot{width:22px;height:22px;border-radius:50%;background:var(--orange)}
  .brand-name{font-family:"Libre Baskerville",serif;font-weight:700;font-size:22px;color:var(--navy-title)}
  .wheel-label{font-family:"Libre Baskerville",serif;font-size:15px;fill:var(--white);text-anchor:middle}
  .wheel-label--side{font-size:12px;text-anchor:start}
  .callout{position:absolute;width:200px;background:var(--panel);border-radius:9px;overflow:hidden}
  .callout-head{font-family:"Libre Baskerville",serif;font-size:15px;color:var(--white);text-align:center;padding:5px 6px 4px;line-height:19px;letter-spacing:.3px}
  .callout--green .callout-head{background:var(--green)}
  .callout--navy .callout-head{background:var(--navy)}
  .callout--orange .callout-head{background:var(--orange)}
  .callout--gray .callout-head{background:var(--gray)}
  .callout-list{list-style:none;font-family:"Lato",sans-serif;font-size:12px;line-height:14.8px;color:var(--ink);padding:7px 8px 9px 26px}
  .callout-list li{position:relative}
  .callout-list li::before{content:"";position:absolute;left:-13px;top:5px;width:5px;height:5px;border-radius:50%}
  .callout--green li::before{background:var(--green)}
  .callout--navy li::before{background:var(--navy)}
  .callout--orange li::before{background:var(--orange)}
  .callout--gray li::before{background:var(--gray)}
  .callout-list--compact{padding-left:16px;font-size:11.5px}
  .page-number{font-family:"Lato",sans-serif;font-size:10px;fill:var(--white);text-anchor:middle}
</style>
</head>
<body>
<main class="canvas">

  <!-- Slide 1: Total Asset Allocation -->
  <section class="slide-frame slide-frame--first">
    <div class="slide">
      <svg class="slide-art" viewBox="0 0 984 553" aria-hidden="true">
        <defs>
          <linearGradient id="wave-a" x1="0" y1="0" x2="0" y2="1">
            <stop offset="0" stop-color="#2aa3c4"/>
            <stop offset="1" stop-color="#146784"/>
          </linearGradient>
        </defs>
        <path d="M38 78 Q150 66 282 70 Q160 72 38 84 Z" fill="var(--orange)"/>
        <g class="connectors" stroke="var(--line)" stroke-width="1" fill="none">
          <path d="M262 149 H392"/>
          <path d="M262 286 H318"/>
          <path d="M741 215 H650"/>
          <path d="M741 344 H728 V442 H575"/>
        </g>
        <g class="wheel">
          <circle cx="493" cy="288" r="160" fill="var(--teal)"/>
          <path d="M493 288 L383.4 147.7 A178 178 0 0 1 602.6 147.7 Z" fill="var(--green)"/>
          <path d="M493 288 L633.3 178.4 A178 178 0 0 1 633.3 397.6 Z" fill="var(--orange)"/>
          <path d="M493 288 L602.6 428.3 A178 178 0 0 1 383.4 428.3 Z" fill="var(--gray)"/>
          <path d="M493 288 L352.7 397.6 A178 178 0 0 1 352.7 178.4 Z" fill="var(--navy)"/>
          <circle cx="493" cy="288" r="54" fill="var(--white)"/>
          <circle cx="493" cy="288" r="46" fill="none" stroke="var(--teal-deep)" stroke-width="5"/>
          <text class="wheel-label" x="493" y="175">PRESERVATION</text>
          <text class="wheel-label" x="376" y="276">CAPITAL</text>
          <text class="wheel-label" x="376" y="296">MARKETS</text>
          <text class="wheel-label" x="601" y="276">REAL</text>
          <text class="wheel-label" x="601" y="296">ESTATE</text>
          <text class="wheel-label" x="490" y="410">ALTERNATIVES</text>
        </g>
        <path d="M0 498 Q120 478 300 488 Q520 512 700 516 Q860 518 984 496 V553 H0 Z" fill="url(#wave-a)"/>
        <circle cx="916" cy="519" r="17" fill="var(--orange)" stroke="#f4c27a" stroke-width="2"/>
        <text class="page-number" x="916" y="523">3</text>
      </svg>

      <h1 class="slide-title">Total Asset Allocation</h1>
      <div class="brand"><span class="brand-dot"></span><span class="brand-name">The Harborline LLC</span></div>

      <div class="callout callout--green" style="left:62px;top:120px">
        <div class="callout-head">PRESERVATION</div>
        <ul class="callout-list"><li>Cash</li><li>Checking/savings accounts</li><li>Money market accounts</li><li>CD's</li><li>Fixed annuities</li></ul>
      </div>
      <div class="callout callout--navy" style="left:62px;top:262px">
        <div class="callout-head">CAPITAL MARKETS</div>
        <ul class="callout-list"><li>Publicly traded stocks and bonds</li></ul>
      </div>
      <div class="callout callout--orange" style="left:741px;top:186px">
        <div class="callout-head">REAL ESTATE</div>
        <ul class="callout-list"><li>Single-family Residence</li><li>Retail</li><li>Industrial</li><li>Multifamily</li><li>Office</li></ul>
      </div>
      <div class="callout callout--gray" style="left:741px;top:317px">
        <div class="callout-head">ALTERNATIVES</div>
        <ul class="callout-list"><li>Private Equity</li><li>Private Credit</li><li>Cryptocurrency</li><li>Asset-backed Loans</li><li>Tax Liens</li><li>Oil &amp; Gas</li><li>Litigation Finance</li><li>Royalties</li></ul>
      </div>
    </div>
  </section>

  <!-- Slide 2: Capital Markets -->
  <section class="slide-frame slide-frame--second">
    <div class="slide">
      <svg class="slide-art" viewBox="0 0 984 553" aria-hidden="true">
        <defs>
          <linearGradient id="wave-b" x1="0" y1="0" x2="0" y2="1">
            <stop offset="0" stop-color="#2aa3c4"/>
            <stop offset="1" stop-color="#146784"/>
          </linearGradient>
        </defs>
        <path d="M98 88 Q220 76 345 80 Q220 82 98 94 Z" fill="var(--orange)"/>
        <g class="connectors" stroke="var(--line)" stroke-width="1" fill="none">
          <path d="M265 149 H392"/>
          <path d="M265 286 H318"/>
          <path d="M743 218 H650"/>
          <path d="M743 345 H726 V444 H575"/>
        </g>
        <g class="wheel">
          <circle cx="493" cy="288" r="160" fill="var(--teal)"/>
          <path d="M493 288 L383.4 147.7 A178 178 0 0 1 602.6 147.7 Z" fill="var(--green)"/>
          <path d="M493 288 L633.3 178.4 A178 178 0 0 1 633.3 397.6 Z" fill="var(--orange)"/>
          <path d="M493 288 L602.6 428.3 A178 178 0 0 1 383.4 428.3 Z" fill="var(--gray)"/>
          <path d="M493 288 L352.7 397.6 A178 178 0 0 1 352.7 178.4 Z" fill="var(--navy)"/>
          <circle cx="493" cy="288" r="54" fill="var(--white)"/>
          <circle cx="493" cy="288" r="46" fill="none" stroke="var(--teal-deep)" stroke-width="5"/>
          <text class="wheel-label" x="493" y="175">FIXED INCOME</text>
          <text class="wheel-label" x="377" y="282">DOMESTIC</text>
          <text class="wheel-label" x="377" y="301">STOCKS</text>
          <text class="wheel-label wheel-label--side" x="552" y="292">ALTERNATIVES</text>
          <text class="wheel-label" x="492" y="411">INTERNATIONAL</text>
          <text class="wheel-label" x="492" y="430">STOCKS</text>
        </g>
        <path d="M0 498 Q120 478 300 488 Q520 512 700 516 Q860 518 984 496 V553 H0 Z" fill="url(#wave-b)"/>
        <circle cx="916" cy="519" r="17" fill="var(--orange)" stroke="#f4c27a" stroke-width="2"/>
        <text class="page-number" x="916" y="523">3</text>
      </svg>

      <h1 class="slide-title">Capital Markets</h1>
      <div class="brand"><span class="brand-dot"></span><span class="brand-name">The Harborline LLC</span></div>

      <div class="callout callout--green" style="left:65px;top:121px">
        <div class="callout-head">FIXED INCOME</div>
        <ul class="callout-list"><li>Corporate</li><li>Municipal</li><li>Government</li><li>Domestic</li><li>International</li></ul>
      </div>
      <div class="callout callout--navy" style="left:65px;top:256px">
        <div class="callout-head">DOMESTIC STOCKS</div>
        <ul class="callout-list"><li>Large, mid, and small companies</li></ul>
      </div>
      <div class="callout callout--orange" style="left:743px;top:189px">
        <div class="callout-head">ALTERNATIVES</div>
        <ul class="callout-list"><li>Metals</li><li>Real Estate</li></ul>
      </div>
      <div class="callout callout--gray" style="left:743px;top:295px">
        <div class="callout-head">INTERNATIONAL<br>STOCKS</div>
        <ul class="callout-list callout-list--compact"><li>Large, mid/small companies</li><li>Developed and emerging regions</li></ul>
      </div>
    </div>
  </section>

</main>
</body>
</html>
```